Estate Planning Law Firm opening new branch in Florida

I am an experienced estate planning attorney that recently relocated to Florida. Looking for a banner Ad to place on platforms such as YardLoop, Chatterly and Pixmora to create publicity for firm and new leads.

```html
<!DOCTYPE html>
<html lang="en">
<head>
<meta charset="utf-8">
<title>Serenova Law Firm – Social Ad Set</title>
<link rel="stylesheet" href="https://fonts.googleapis.com/css2?family=Cinzel:wght@700;800;900&family=Montserrat:wght@500&family=Roboto:wght@400;700&display=swap">
<style>
:root{
  --sheet:#d6d7d9;
  --teal:#1b6b6f;
  --navy:#2a3a4d;
  --accent:#2fc3c3;
  --ink:#1d1d1d;
  --body:#3c3c3c;
  --white:#ffffff;
}
*{margin:0;padding:0;box-sizing:border-box}
html,body{width:811px;height:1200px;overflow:hidden;background:var(--sheet)}
.sheet{position:relative;width:811px;height:1200px}
.ad{position:absolute;width:378px;height:378px;background:var(--white);overflow:hidden}
.ad--1{left:16px;top:16px}.ad--2{left:414px;top:16px}
.ad--3{left:16px;top:411px}.ad--4{left:414px;top:411px}
.ad--5{left:16px;top:807px}.ad--6{left:414px;top:807px}
.ad__shapes{position:absolute;inset:0;width:378px;height:378px}
.t{position:absolute}
.brand{position:absolute;text-align:center;color:var(--teal);font-family:"Cinzel",serif;font-weight:800;font-size:17px;line-height:1;letter-spacing:.3px;white-space:nowrap}
.brand--light{color:var(--white)}
.brand__tag{display:block;font-family:"Roboto",sans-serif;font-weight:400;font-size:5px;letter-spacing:.4px;margin-top:2px;padding-left:13px}
.brand__tag::before,.brand__tag::after{content:"";display:inline-block;width:12px;height:.6px;background:currentColor;vertical-align:middle;margin:0 3px}
.brand__mark{display:inline-block;width:9px;height:9px;background:currentColor;margin-right:4px;vertical-align:1px}
.headline{font-family:"Cinzel",serif;font-weight:900;color:var(--teal);line-height:1.08;white-space:nowrap}
.sub{font-family:"Cinzel",serif;font-weight:800;color:var(--ink);line-height:1.15;white-space:nowrap}
.role{font-family:"Montserrat",sans-serif;font-weight:500;color:var(--ink);letter-spacing:2.6px;white-space:nowrap}
.copy{font-family:"Roboto",sans-serif;font-size:6.6px;line-height:1.13;color:var(--body)}
.contact{position:absolute;font-family:"Montserrat",sans-serif;font-weight:500;font-size:9.4px;letter-spacing:1.1px;color:var(--white);line-height:13.6px;white-space:nowrap}
.contact__label{font-family:"Cinzel",serif;font-weight:800;font-size:11.5px;letter-spacing:.6px;color:var(--accent);line-height:14px}
.right{text-align:right}.center{text-align:center}
</style>
</head>
<body>
<main class="sheet">

<section class="ad ad--1">
  <svg class="ad__shapes" viewBox="0 0 378 378">
    <path d="M0,0 H230 Q190,25 155,60 Q80,35 0,45 Z" fill="var(--teal)"/>
    <path d="M230,0 H245 Q200,30 158,62 L152,58 Q190,25 230,0 Z" fill="var(--navy)"/>
    <path d="M0,48 Q90,40 155,52 Q194,150 184,240 Q130,300 0,300 Z" fill="#7b5d4b" role="img" aria-label="Photo of the two firm partners smiling outdoors"/>
    <path d="M182,265 Q290,272 378,292 V378 H0 V310 Q110,312 182,265 Z" fill="var(--navy)"/>
    <path d="M190,276 Q290,282 378,305 V378 H0 V320 Q120,322 190,276 Z" fill="var(--teal)"/>
  </svg>
  <div class="brand" style="right:30px;top:24px"><span class="brand__mark"></span>SERENOVA<span class="brand__tag">LAW FIRM, PLLC</span></div>
  <div class="t headline right" style="right:26px;top:56px;font-size:30.5px">DISCOVER<br>SERENOVA<br>LAW FIRM</div>
  <div class="t sub right" style="right:28px;top:164px;font-size:11px">YOUR TRUSTED PARTNER<br>IN ESTATE PLANNING</div>
  <p class="t copy right" style="right:26px;top:198px;width:152px">Our mission is to bring peace of mind to working families through comprehensive estate planning, wealth management, and tax planning services. We believe that everyone deserves the security of a well-crafted estate plan, not just the wealthy. Our experienced team is dedicated to ensuring your loved ones are protected and your legacy endures.</p>
  <div class="contact right" style="right:26px;top:312px"><div class="contact__label">More Info</div>shieldandgrowestate.com<br>(555) 014-2290<br>support@serenova.law</div>
</section>

<section class="ad ad--2">
  <svg class="ad__shapes" viewBox="0 0 378 378">
    <path d="M145,0 H378 V128 Q330,90 250,72 Q220,40 145,0 Z" fill="var(--teal)"/>
    <path d="M250,62 Q330,80 378,118 V128 Q330,90 250,72 Z" fill="var(--navy)"/>
    <path d="M0,0 H200 Q188,150 203,240 Q120,275 0,262 Z" fill="#c8c1b6" role="img" aria-label="Photo of two colleagues reviewing work on a laptop"/>
    <path d="M0,262 Q150,262 230,258 Q320,270 378,292 V378 H0 Z" fill="var(--navy)"/>
    <path d="M0,270 Q160,270 235,270 Q320,282 378,305 V378 H0 Z" fill="var(--teal)"/>
  </svg>
  <div class="brand brand--light" style="right:20px;top:24px"><span class="brand__mark"></span>SERENOVA<span class="brand__tag">LAW FIRM, PLLC</span></div>
  <div class="t headline right" style="right:22px;top:124px;font-size:24px;line-height:1">FINANCIAL</div>
  <div class="t headline right" style="right:22px;top:148px;font-size:11px;line-height:1.2">PLANNING AND WEALTH<br>MANAGEMENT SERVICES</div>
  <div class="t sub right" style="right:24px;top:180px;font-size:9.6px">MINIMIZING TAXES<br>AND MAXIMIZING GROWTH</div>
  <div class="t right" style="right:24px;top:209px;font-family:Roboto,sans-serif;font-weight:700;font-size:5.4px;letter-spacing:.8px;color:var(--teal);white-space:nowrap">WHY PROFESSIONAL TAX ADVICE MATTERS</div>
  <p class="t copy right" style="right:23px;top:220px;width:145px">Getting professional tax advice is one of the best ways to be smart about your hard-earned money. Working with our tax advisor, Graham Varden, can help you potentially maximize deductions, prepare for contribution withdrawals, and navigate complex situations.</p>
  <div class="contact right" style="right:24px;top:312px"><div class="contact__label">More Info</div>shieldandgrowestate.com<br>(555) 014-2290<br>support@serenova.law</div>
</section>

<section class="ad ad--3">
  <svg class="ad__shapes" viewBox="0 0 378 378">
    <path d="M190,0 H378 V52 Q300,58 265,72 Q230,30 190,0 Z" fill="var(--teal)"/>
    <path d="M132,0 H150 Q200,50 262,75 L255,78 Q180,40 132,0 Z" fill="var(--navy)"/>
    <path d="M222,62 Q300,50 378,56 V300 Q300,310 256,312 Q215,230 222,62 Z" fill="#7f8b5c" role="img" aria-label="Photo of a multi-generation family walking together outdoors"/>
    <path d="M0,290 Q120,285 220,300 Q250,318 270,330 Q330,335 378,325 V378 H0 Z" fill="var(--navy)"/>
    <path d="M0,302 Q120,298 215,312 Q245,328 268,338 Q330,342 378,335 V378 H0 Z" fill="var(--teal)"/>
  </svg>
  <div class="brand" style="left:26px;top:24px"><span class="brand__mark"></span>SERENOVA<span class="brand__tag">LAW FIRM, PLLC</span></div>
  <div class="t headline" style="left:26px;top:56px;font-size:30px">ESTATE<br>PLANNING<br>SERVICES</div>
  <div class="t sub" style="left:26px;top:164px;font-size:11px">SECURE YOUR FAMILY’S<br>FUTURE WITH SERENOVA</div>
  <p class="t copy" style="left:26px;top:198px;width:140px">Estate planning is a vital step in ensuring your family’s future and the legacy you want to leave behind. At Serenova, we understand that estate planning can seem overwhelming, but with the right guidance, it can provide peace of mind and security for you and your loved ones. Estate Attorney Clara Varden and our team are dedicated to helping you protect your assets, plan for the future, and create a lasting legacy.</p>
  <div class="contact" style="left:26px;top:310px"><div class="contact__label">More Info</div>shieldandgrowestate.com<br>(555) 014-2290<br>support@serenova.law</div>
</section>

<section class="ad ad--4">
  <svg class="ad__shapes" viewBox="0 0 378 378">
    <path d="M0,0 H260 Q185,20 160,52 Q60,70 0,130 Z" fill="var(--teal)"/>
    <path d="M0,118 Q60,60 160,45 L165,52 Q70,70 0,132 Z" fill="var(--navy)"/>
    <path d="M178,40 Q275,5 378,10 V245 Q330,255 230,260 Q160,150 178,40 Z" fill="#3a2a1c" role="img" aria-label="Photo of a rolled banknote resting on wooden blocks spelling tax"/>
    <path d="M0,295 Q120,270 220,262 Q300,256 378,262 V378 H0 Z" fill="var(--navy)"/>
    <path d="M0,305 Q120,282 228,275 Q300,270 378,275 V378 H0 Z" fill="var(--teal)"/>
  </svg>
  <div class="brand brand--light" style="left:22px;top:24px"><span class="brand__mark"></span>SERENOVA<span class="brand__tag">LAW FIRM, PLLC</span></div>
  <div class="t headline" style="left:21px;top:124px;font-size:14.5px;line-height:1">COMPREHENSIVE<br>TAX PLANNING</div>
  <div class="t sub" style="left:21px;top:166px;font-size:9.2px">TAILORED TAX STRATEGIES<br>FOR YOUR FINANCIAL SUCCESS</div>
  <p class="t copy" style="left:21px;top:193px;width:158px">Navigating the complexities of tax planning can be daunting, but with Serenova, you have a trusted partner to guide you through every step. Our comprehensive tax planning services in Coral Haven, Florida are designed to ensure that your financial decisions today pave the way for a secure and prosperous future. After all, you want to be sure that as much of your assets as possible go to care for you in your golden years, and what is left over goes to your family.</p>
  <div class="contact" style="left:21px;top:310px"><div class="contact__label">More Info</div>shieldandgrowestate.com<br>(555) 014-2290<br>support@serenova.law</div>
</section>

<section class="ad ad--5">
  <svg class="ad__shapes" viewBox="0 0 378 378">
    <path d="M0,0 H378 V162 Q250,155 150,178 Q90,105 0,95 Z" fill="var(--teal)"/>
    <path d="M150,170 Q250,150 378,155 V165 Q250,160 150,182 Z" fill="var(--navy)"/>
    <path d="M0,100 Q50,90 70,93 Q140,130 190,228 Q180,320 170,378 H0 Z" fill="#87857a" role="img" aria-label="Portrait photo of the firm's attorney"/>
  </svg>
  <div class="brand brand--light" style="left:26px;top:24px"><span class="brand__mark"></span>SERENOVA<span class="brand__tag">LAW FIRM, PLLC</span></div>
  <div class="t headline center" style="left:140px;width:240px;top:50px;font-size:16.5px;line-height:1;color:var(--white)">CONSULTING<br>SERVICES</div>
  <p class="t copy center" style="left:140px;width:230px;top:88px;color:var(--white);font-size:6.9px">We know lawyers aren’t the only answer. Serenova Law Firm, PLLC is affiliated with Serenova Financial LLC consulting firm which provides strategic services that complement and enhance our legal services. By collaborating with our affiliates, we provide clients with a financial consultant who understands your financial planning strategies and a lawyer who understands your long-term estate planning strategies. We offer a cohesive, big-picture approach and innovative solutions.</p>
  <div class="t headline right" style="right:24px;top:192px;font-size:23px;line-height:1">ATTORNEY<br>CLARA<br>VARDEN</div>
  <div class="t role right" style="right:24px;top:271px;font-size:10.5px">ATTORNEY AT LAW</div>
  <div class="contact right" style="right:30px;top:311px;color:var(--ink)"><div class="contact__label" style="color:var(--teal)">More Info</div>shieldandgrowestate.com<br>(555) 014-2290<br>support@serenova.law</div>
</section>

<section class="ad ad--6">
  <svg class="ad__shapes" viewBox="0 0 378 378">
    <path d="M0,0 H220 Q190,60 185,100 Q90,90 0,68 Z" fill="var(--teal)"/>
    <path d="M0,62 Q90,82 186,92 L186,102 Q90,92 0,74 Z" fill="var(--navy)"/>
    <path d="M230,0 H378 V300 Q320,292 270,290 Q205,230 195,150 Q190,40 230,0 Z" fill="#8b735f" role="img" aria-label="Portrait photo of the financial planner"/>
    <path d="M0,340 Q150,300 378,290 V378 H0 Z" fill="var(--navy)"/>
    <path d="M0,352 Q160,312 378,302 V378 H0 Z" fill="var(--teal)"/>
  </svg>
  <div class="brand" style="left:24px;top:24px"><span class="brand__mark"></span>SERENOVA<span class="brand__tag">LAW FIRM, PLLC</span></div>
  <div class="t headline" style="left:24px;top:140px;font-size:24px;line-height:.95">GRAHAM<br>VARDEN</div>
  <div class="t role" style="left:27px;top:192px;font-size:10px">FINANCIAL PLANNER</div>
  <div class="t sub" style="left:27px;top:214px;font-size:9.2px">CONSULTING SERVICES</div>
  <p class="t copy" style="left:27px;top:229px;width:160px">We know lawyers aren’t the only answer. Serenova Law Firm, PLLC is affiliated with Serenova Financial LLC consulting firm which provides strategic services that complement and enhance our legal services. By collaborating with our affiliates, we provide clients with a financial consultant who understands your financial planning strategies and a lawyer who understands your long-term estate planning strategies. We offer a cohesive, big-picture approach and innovative solutions.</p>
  <div class="contact right" style="right:30px;top:311px"><div class="contact__label">More Info</div>shieldandgrowestate.com<br>(555) 014-2290<br>support@serenova.law</div>
</section>

</main>
</body>
</html>
```